"Drink Champagne and Dance on the Table" sort of business card needed!

We throw events, weddings, engagement parties, baby showers and the sort of end of year corporate events that people remember long after the glitter has settled - the sort of events that make you stand still and say wow when you walk in and then make you want to "Drink Champagne and Dance on the Tables"

We have a great logo with heaps of potential and need a business card that just screams creative professionals!

We are based in Auckland, NZ and are priced at the Premium end of the market were there are around 10 other main competitors. We need to stand out and make a strong statement about who we are!

Our Business Card will be one of the few items that we print out so are fully prepared to invest in a premium print job.

We really love our logo and think it has heaps of potential! Its ok if you would like to manipulate it (maybe put it on an angle, or use the circle element on its own?).

Black and Gold is very striking, but its very done in our market so we would like to avoid a solid black background please

We have done a bit of an inspiration document to give you an idea of the sort of look and feel we are hoping to achieve.

Target Market(s)

Woman aged 30 - 45 with an income bracket of $70k +

Industry/Entity Type

Event Planning

Contact Information for Business Card

Marnie
hello@fennoriwick.co.nz
www.fennoriwick.co.nz
02734419027

Number of Pages Required

5+ page

Requirements
Must have
• Vibrant colours and design (we love the vibrant pink and gold in the inspiration file)
• We would love to see some colour and creativity (although the black and gold is very striking). Because we are doing such minimal print work I am happy for the cards to be a little more expensive so if you want to use cut outs, rounded corners, gold foil, non standard size etc I am happy for that too. I really want the wow factor.
Nice to have
• We would like the design to be double sided.
Should not have
• The logo colour changed
• Use of Purple or Green or solid black background.
• Wedding Photos!

```html
<!DOCTYPE html>
<html lang="en">
<head>
<meta charset="utf-8">
<title>Fenno and Riwick – Business Card</title>
<link rel="stylesheet" href="https://fonts.googleapis.com/css2?family=Josefin+Sans:wght@300;400&display=swap">
<style>
  :root {
    --page-bg: #2a2420;
    --pink-deep: #b0155a;
    --pink-bright: #e8457f;
    --rose-deep: #5e0f33;
    --rose-light: #8e2352;
    --gold: #e2bb55;
    --gold-light: #f6dc8a;
    --gold-deep: #b08628;
  }
  * { margin: 0; padding: 0; box-sizing: border-box; }
  html, body {
    width: 1200px; height: 813px; overflow: hidden;
    background: var(--page-bg);
    font-family: "Josefin Sans", sans-serif;
  }
  .canvas {
    width: 1200px; height: 813px;
    display: flex; align-items: center; justify-content: center; gap: 28px;
  }
  .card {
    position: relative;
    width: 558px; height: 322px;
    border-radius: 18px;
    overflow: hidden;
    box-shadow: 0 14px 30px rgba(0,0,0,.45);
  }
  .card--front {
    background: linear-gradient(100deg, var(--pink-deep) 0%, var(--pink-bright) 100%);
  }
  .card--back {
    background: linear-gradient(100deg, var(--rose-deep) 0%, var(--rose-light) 100%);
  }
  .card__arcs { position: absolute; inset: 0; }
  .brand {
    position: absolute;
    display: flex; align-items: center; gap: 10px;
    color: var(--gold);
    font-weight: 400;
    white-space: nowrap;
  }
  .brand__dot {
    flex: none;
    border: 2px solid var(--gold);
    border-radius: 50%;
  }
  .card--front .brand {
    left: 50%; top: 50%; transform: translate(-50%, -50%);
    font-size: 28px;
  }
  .card--front .brand__dot { width: 34px; height: 34px; }
  .card--back .brand {
    left: 34px; top: 50%; transform: translateY(-50%);
    font-size: 20px;
  }
  .card--back .brand__dot { width: 26px; height: 26px; }
  .contact {
    position: absolute; left: 292px; top: 96px;
    color: var(--gold);
  }
  .contact__name {
    font-size: 24px; font-weight: 300; letter-spacing: 1.5px;
    margin-bottom: 10px;
  }
  .contact__line {
    display: flex; align-items: center; gap: 9px;
    font-size: 15px; font-weight: 300; letter-spacing: .5px;
    margin-bottom: 7px;
  }
  .contact__icon { width: 14px; height: 14px; flex: none; }
</style>
</head>
<body>
<main class="canvas">

  <section class="card card--front" aria-label="Card front">
    <svg class="card__arcs" viewBox="0 0 558 322" aria-hidden="true">
      <defs>
        <linearGradient id="goldSheen" x1="0" y1="0" x2="1" y2="1">
          <stop offset="0" stop-color="#f6dc8a"/>
          <stop offset=".5" stop-color="#e2bb55"/>
          <stop offset="1" stop-color="#b08628"/>
        </linearGradient>
      </defs>
      <circle cx="279" cy="161" r="225" fill="none" stroke="url(#goldSheen)" stroke-width="13"/>
      <circle cx="279" cy="161" r="250" fill="none" stroke="url(#goldSheen)" stroke-width="6"/>
    </svg>
    <div class="brand">
      <span class="brand__dot"></span>
      <span class="brand__name">Fenno and Riwick</span>
    </div>
  </section>

  <section class="card card--back" aria-label="Card back">
    <div class="brand">
      <span class="brand__dot"></span>
      <span class="brand__name">Fenno and Riwick</span>
    </div>
    <div class="contact">
      <p class="contact__name">Marnie</p>
      <p class="contact__line">
        <svg class="contact__icon" viewBox="0 0 14 14" aria-hidden="true">
          <rect x="1" y="3" width="12" height="8" fill="none" stroke="#e2bb55" stroke-width="1.2"/>
          <path d="M1 3l6 5 6-5" fill="none" stroke="#e2bb55" stroke-width="1.2"/>
        </svg>
        hello@fennoriwick.co.nz
      </p>
      <p class="contact__line">
        <svg class="contact__icon" viewBox="0 0 14 14" aria-hidden="true">
          <circle cx="7" cy="7" r="5.5" fill="none" stroke="#e2bb55" stroke-width="1.2"/>
          <ellipse cx="7" cy="7" rx="2.4" ry="5.5" fill="none" stroke="#e2bb55" stroke-width="1"/>
          <path d="M1.5 7h11" stroke="#e2bb55" stroke-width="1"/>
        </svg>
        www.fennoriwick.co.nz
      </p>
      <p class="contact__line">
        <svg class="contact__icon" viewBox="0 0 14 14" aria-hidden="true">
          <path d="M1 5c0-2 2.5-3 6-3s6 1 6 3v1h-3V4.5H4V6H1z" fill="#e2bb55"/>
          <rect x="2.5" y="7" width="9" height="5.5" rx="1" fill="#e2bb55"/>
        </svg>
        02734419027
      </p>
    </div>
  </section>

</main>
</body>
</html>
```